Delwyn's Pressure Washing Services

Starting a pressure washing business on my own in Central Valley California, not too much experience so affordable, I do houses, fences, driveways, cars, trailers, RVs. Planning to make this full-time hoping clientele picks up after having a nice business card. Design doesn't have to be flashy, more to the point, I like simplistic/personable. I do not want something exhausting to look at or with too much going on.

Target Market(s)

Residential, Commercial

Industry/Entity Type

Pressure Washing

Contact Information for Business Card

avalible Services

Font styles to use
Sans Serif

Colors
0054AA
0677BA
7BADD7
CADEEF
E8F1F8
0094D4
00A9DD
6FCCEA
C7EBF8
E9F6FB
00AB8E
00BBA5
67D7C9
C6EFE9
E9F9F6

```html
<!DOCTYPE html>
<html lang="en">
<head>
<meta charset="utf-8">
<title>Delwyn's Pressure Washing Services – Business Card</title>
<link rel="stylesheet" href="https://fonts.googleapis.com/css2?family=Montserrat:wght@700;800&display=swap">
<style>
  :root {
    --navy: #0f4a9e;
    --navy-deep: #0b3d86;
    --blue-bright: #1aa0dc;
    --sky: #3aa6e0;
    --sky-pale: #e9f6fb;
    --orange: #c98a2f;
    --white: #ffffff;
    --dot: #5cc3ec;
    --backdrop: #e9e4dc;
    --mascot-a: #2a4f9a;
    --mascot-b: #c98a2f;
  }
  * { box-sizing: border-box; margin: 0; padding: 0; }
  html, body { width: 900px; height: 1200px; overflow: hidden; }
  body {
    background: var(--backdrop);
    font-family: "Montserrat", Arial, sans-serif;
    position: relative;
  }
  .card {
    position: absolute;
    left: 73px;
    width: 762px;
    height: 446px;
    border-radius: 30px;
    overflow: hidden;
    box-shadow: 0 6px 16px rgba(0,0,0,.25);
  }
  .card--front { top: 112px; }
  .card--back { top: 636px; }
  .card__shapes { position: absolute; inset: 0; width: 100%; height: 100%; }

  .mascot {
    position: absolute;
    border-radius: 40px 40px 20px 20px;
    background: linear-gradient(180deg, var(--mascot-b) 0%, var(--mascot-b) 35%, var(--mascot-a) 36%, var(--mascot-a) 100%);
    opacity: .9;
  }
  .card--front .mascot { left: 62px; top: 40px; width: 200px; height: 355px; }
  .card--back .mascot { left: 150px; top: 45px; width: 105px; height: 215px; }

  .owner {
    position: absolute;
    right: 42px;
    top: 64px;
    text-align: right;
    color: var(--white);
  }
  .owner__name { font-size: 29px; font-weight: 800; letter-spacing: .5px; }
  .owner__phone {
    margin-top: 6px;
    font-size: 22px;
    font-weight: 700;
    display: flex;
    align-items: center;
    justify-content: flex-end;
    gap: 6px;
  }
  .owner__phone svg { width: 17px; height: 17px; }

  .brand {
    position: absolute;
    display: flex;
    align-items: center;
    gap: 14px;
  }
  .brand__name {
    font-weight: 800;
    line-height: 1.1;
    text-transform: uppercase;
  }
  .brand__dot { border-radius: 50%; background: var(--dot); flex: none; }

  .card--front .brand { left: 338px; top: 282px; }
  .card--front .brand__name { color: var(--white); font-size: 30px; }
  .card--front .brand__dot { width: 22px; height: 22px; }

  .card--back .brand { left: 275px; top: 150px; }
  .card--back .brand__name { color: var(--navy); font-size: 25px; }
  .card--back .brand__dot { width: 18px; height: 18px; }

  .services {
    position: absolute;
    left: 0; right: 0;
    top: 350px;
    text-align: center;
    color: var(--white);
    font-size: 22px;
    font-weight: 800;
    line-height: 30px;
    letter-spacing: .6px;
  }
  .services__sep {
    display: inline-block;
    width: 8px; height: 8px;
    border-radius: 50%;
    background: var(--dot);
    margin: 0 7px;
    vertical-align: middle;
    position: relative; top: -2px;
  }
</style>
</head>
<body>

<section class="card card--front">
  <svg class="card__shapes" viewBox="0 0 762 446" preserveAspectRatio="none">
    <defs>
      <radialGradient id="skyGlow" cx="30%" cy="40%" r="75%">
        <stop offset="0%" stop-color="#ffffff"/>
        <stop offset="55%" stop-color="#bfe2f5"/>
        <stop offset="100%" stop-color="#3aa6e0"/>
      </radialGradient>
      <linearGradient id="navyFade" x1="0" y1="0" x2="1" y2="1">
        <stop offset="0%" stop-color="#0b3d86"/>
        <stop offset="70%" stop-color="#1150a8"/>
        <stop offset="100%" stop-color="#1aa0dc"/>
      </linearGradient>
    </defs>
    <rect width="762" height="446" fill="var(--orange)"/>
    <path d="M0,0 H440 Q462,12 442,48 L130,446 H0 Z" fill="url(#skyGlow)" stroke="#ffffff" stroke-width="6"/>
    <path d="M762,186 H440 Q392,188 362,232 L186,446 H762 Z" fill="url(#navyFade)" stroke="#ffffff" stroke-width="5"/>
  </svg>

  <div class="mascot" role="img" aria-label="Cartoon mascot of a pressure washer in cap and overalls spraying water"></div>

  <div class="owner">
    <div class="owner__name">DELWYN MORA</div>
    <div class="owner__phone">
      <svg viewBox="0 0 24 24" fill="none" stroke="currentColor" stroke-width="2.4" stroke-linecap="round" stroke-linejoin="round" aria-hidden="true">
        <path d="M5 3h4l2 5-2.5 1.5a11 11 0 0 0 6 6L16 13l5 2v4a2 2 0 0 1-2 2A16 16 0 0 1 3 5a2 2 0 0 1 2-2z"/>
      </svg>
      2099 482 317
    </div>
  </div>

  <div class="brand">
    <div class="brand__name">Delwyn's<br>Pressure Washing<br>Services</div>
    <span class="brand__dot"></span>
  </div>
</section>

<section class="card card--back">
  <svg class="card__shapes" viewBox="0 0 762 446" preserveAspectRatio="none">
    <rect width="762" height="446" fill="var(--navy)"/>
    <path d="M0,0 H732 Q718,24 716,70 L706,236 Q698,318 612,318 H0 Z" fill="var(--orange)"/>
    <path d="M0,0 H718 Q704,24 702,70 L692,232 Q684,302 600,302 H0 Z" fill="#ffffff"/>
  </svg>

  <div class="mascot" role="img" aria-label="Cartoon mascot of a pressure washer in cap and overalls spraying water"></div>

  <div class="brand">
    <div class="brand__name">Delwyn's<br>Pressure Washing<br>Services</div>
    <span class="brand__dot"></span>
  </div>

  <div class="services">
    HOUSES<span class="services__sep"></span>FENCES<span class="services__sep"></span>DRIVEWAYS<span class="services__sep"></span>CARS<br>
    TRAILERS<span class="services__sep"></span>RVS
  </div>
</section>

</body>
</html>
```